In need of a Wordpress website for a Water Sports Rental Company!

We are starting a new venture that provides a variety of rental equipment in the Cayman Islands. We are in need of a website where guests are able to book their rental gear during their stay in Cayman. We will also have an interactive map where guests can learn about off the beaten path activities to explore in here Cayman.

Our target market is middle/upper class, so we need a website that appeals to this group. We need our website to be clean, simple and easy to navigate. We need it to be highly visual and modern. We like the idea of the website having a tropical feel to it, we are very open to creative ideas that reflects this!

Must be designed in WordPress using the Quelmira template I’ve provided.

You will find all instructions & the photos I want to use for this website on the following vaultra account:
- www.vaultra.com
- Username: fun@marlettoboats.com
- Password: lantern4

All of the photos will need to be resized accordingly to be as small as possible without loosing resolution.

These are the tabs that will be used:
- Home Page
- Adventure Map
- Rental Gear
- Tours
- Photo Gallery
- Contact Us

Home Page
- You will find all the text and instructions for the home page in the word document named ‘Home Page’.

Adventure Map
- You will find all the text and instructions for the home page in the word document named ‘Adventure Map Content’
- There will also be a few 'guide' pages under this tab, which we will go in to detail with the winner.

Rentals
- You will find all the text and instructions for the Rentals page in the word document named ‘Rentals Content’

Tours
- This will just be a page saying ‘kayaking, snorkeling & Bioluminescence tours coming soon’.

Photo Gallery
- You will find the photos for this in our Vaultra.com Account

Contact Us
- Send us a Message – page will be similar to our other site http://marlettoboats.com/contact/
- Phone: +1 (345) 555 0182
- Email: fun@zolvatrek.com

The big factors on who will have the winning design are:
- The background used
- The layout of the Home Page
- The animations at the top of the Rental Landing Page
- The overall clean, professional look to the website

If you have any questions, don't hesitate to ask.

We look forward to working with you all!!

Good luck!!

Target Market(s)

Middle/Upper Class on vacation with their family

Industry/Entity Type

It Company

Coding

Coded - Design and coding required

Number of Pages Required

5+ page

Colors
fffbf0
cadf82
fbf289
f6faec
fdf9cf
eaf2ce
fff3d1
fee18a
abd037

Requirements
Must have
• - Must be designed in Wordpress using the Quelmira template I have provided or another suitable web template.
• - Must be Responsive Web Design so that the website adjusts to various screen sizes.

```html
<!DOCTYPE html>
<html lang="en">
<head>
<meta charset="utf-8">
<title>Zolvatrek – Private Boat Charter Adventures</title>
<link href="https://fonts.googleapis.com/css2?family=Alfa+Slab+One&family=Libre+Baskerville:wght@400;700&family=Lato:wght@400;700&display=swap" rel="stylesheet">
<style>
:root{
  --teal:#14977c;
  --teal-dark:#0d7560;
  --lime:#9dbb3f;
  --ink:#1f2326;
  --body:#555b60;
  --mist:#eef0ef;
  --paper:#ffffff;
  --sea-deep:#1f6f8f;
  --sea-light:#5fc3c9;
}
*{box-sizing:border-box;margin:0;padding:0}
html,body{width:1200px;height:5373px;overflow:hidden;background:var(--paper)}
body{position:relative;font-family:"Lato",Arial,sans-serif;color:var(--body);font-size:14px;line-height:1.6}
.abs{position:absolute}
.serif{font-family:"Libre Baskerville",Georgia,serif}

/* header */
.site-header{left:0;top:0;width:1200px;height:168px;background:var(--paper)}
.brand{left:0;width:1200px;top:22px;display:flex;justify-content:center;align-items:center;gap:12px}
.brand-dot{width:64px;height:64px;border-radius:50%;background:var(--teal)}
.brand-name{font-family:"Lato",sans-serif;font-weight:700;font-size:30px;color:var(--teal-dark);letter-spacing:1px}
.main-nav{left:0;top:128px;width:1200px;height:40px;border-top:1px solid #e4e4e4;display:flex;justify-content:center;gap:46px;font-size:14px;color:var(--ink);padding-top:10px}
.main-nav .active{color:var(--teal);border-bottom:2px solid var(--teal)}

/* hero */
.hero{left:0;top:168px;width:1200px;height:532px;background:linear-gradient(180deg,#7fd4d8 0%,#3fa7b8 40%,#1d6f8a 100%)}
.hero-title{left:0;top:350px;width:1200px;text-align:center;font-family:"Alfa Slab One",serif;font-size:44px;line-height:54px;color:#fff;text-shadow:0 2px 6px rgba(0,0,0,.35)}
.hero-btn{left:474px;top:578px;width:252px;height:48px;border:2px solid #fff;background:rgba(0,0,0,.35);color:#fff;display:flex;align-items:center;justify-content:center;gap:10px;font-weight:700;font-size:15px}

/* feature cards */
.feature{top:727px;width:330px;height:225px;background:#fff;box-shadow:0 4px 12px rgba(0,0,0,.12);text-align:center}
.feature .photo{height:130px;width:100%}
.feature h3{font-family:"Libre Baskerville",serif;font-size:17px;color:var(--ink);margin-top:12px}
.feature p{font-size:13px;padding:6px 36px 0;line-height:1.5}

/* about */
.about-title{left:0;top:1000px;width:1200px;text-align:center;font-family:"Libre Baskerville",serif;font-weight:700;font-size:38px;color:var(--ink)}
.about-title span{color:var(--lime);font-weight:400}
.about-text{left:80px;top:1065px;width:1040px;font-size:13px;line-height:1.65}
.btn-outline{left:525px;top:1170px;width:150px;height:48px;border:2px solid var(--ink);display:flex;align-items:center;justify-content:center;font-weight:700;color:var(--ink);font-size:15px}

/* video band */
.video-band{left:0;top:1250px;width:1200px;height:680px}
.video-frame{left:222px;top:1290px;width:756px;height:362px;background:linear-gradient(160deg,#2b8e8e,#0f4e5c);border:6px solid #0d6f5a}
.play{left:555px;top:1426px;width:90px;height:90px}
.video-title{left:0;top:1762px;width:1200px;text-align:center;font-family:"Libre Baskerville",serif;font-weight:700;font-size:26px;color:#fff}
.video-text{left:220px;top:1815px;width:760px;text-align:center;color:#fff;font-weight:700;font-size:13px;line-height:1.55}

/* gallery */
.section-title{left:0;width:1200px;text-align:center;font-family:"Libre Baskerville",serif;font-weight:700;font-size:38px;color:var(--ink)}
.section-title span{color:var(--lime);font-weight:400}
.gallery-photo{border:4px solid #fff;box-shadow:0 2px 6px rgba(0,0,0,.15)}

/* alternating features */
.strip{left:0;width:1200px;height:307px;background:linear-gradient(135deg,#f3f4f3,#e2e5e4)}
.strip svg.band{position:absolute;left:0;top:0}
.strip .circle{position:absolute;top:11px;width:285px;height:285px;border-radius:50%;border:8px solid #fff;box-shadow:0 4px 14px rgba(0,0,0,.2)}
.strip .copy{position:absolute;top:70px}
.strip h2{font-family:"Libre Baskerville",serif;font-weight:700;font-size:26px;line-height:1.3;color:var(--ink)}
.strip.left h2{color:var(--teal)}
.strip p{font-size:13px;line-height:1.6;margin-top:12px}

/* top picks */
.pick{top:4745px;width:250px}
.pick .photo{height:250px;width:100%}
.pick h4{font-family:"Libre Baskerville",serif;font-weight:700;font-size:19px;color:var(--ink);margin-top:14px}
.pick p{font-size:13px;line-height:1.5;margin-top:4px}

/* footer */
.site-footer{left:0;top:5150px;width:1200px;height:223px;background:#eceeed}
.footer-nav{left:75px;top:5195px;display:flex;gap:30px;font-size:13px;color:var(--ink)}
.footer-brand{left:555px;top:5160px;width:90px;height:90px;border-radius:50%;background:var(--teal);border:5px solid #fff}
.footer-name{left:0;top:5253px;width:1200px;text-align:center;font-weight:700;font-size:12px;color:var(--teal-dark)}
.social{top:5185px;width:40px;height:40px;background:var(--teal)}
.footer-rule{left:75px;top:5240px;width:1050px;border-top:1px solid #cfd3d2}
.contact-item{top:5285px;display:flex;align-items:flex-start;gap:10px;font-size:13px;color:var(--ink)}
.copyright{left:0;top:5343px;width:1200px;text-align:center;font-size:12px;color:var(--ink)}
.copyright b{color:var(--teal-dark)}
</style>
</head>
<body>

<header class="site-header abs">
  <div class="brand abs"><span class="brand-dot"></span><span class="brand-name">ZOLVATREK</span></div>
  <nav class="main-nav abs">
    <span class="active">Home</span><span>Adventure Map</span><span>Rental Gear</span><span>Tours</span><span>Gallery</span><span>Contact Us</span>
  </nav>
</header>

<section class="hero abs" role="img" aria-label="Snorkeler swimming among tropical fish in clear Caribbean water"></section>
<h1 class="hero-title abs">Private Boat Charter Adventures<br>in the Cayman Islands</h1>
<div class="hero-btn abs">
  <svg width="20" height="20" viewBox="0 0 20 20"><circle cx="10" cy="10" r="9" fill="none" stroke="#fff" stroke-width="2"/><path d="M8 6l6 4-6 4z" fill="#fff"/></svg>
  Watch Our Video First
</div>

<article class="feature abs" style="left:79px">
  <div class="photo" role="img" aria-label="Kayakers paddling on turquoise water" style="background:linear-gradient(180deg,#9fd6ee,#3bb5c4)"></div>
  <h3>Exploration</h3>
  <p>Rent everything you need to get outside and explore the island on your own terms.</p>
</article>
<article class="feature abs" style="left:435px">
  <div class="photo" role="img" aria-label="Calm beach shoreline with shallow water" style="background:linear-gradient(180deg,#c7e9ee,#7fcfc4)"></div>
  <h3>Relaxation</h3>
  <p>We will come straight to your resort or condo and set everything up for you and your family.</p>
</article>
<article class="feature abs" style="left:791px">
  <div class="photo" role="img" aria-label="Island coastline with palm trees and lagoon" style="background:linear-gradient(180deg,#8cc7e4,#2e9e9a)"></div>
  <h3>Education</h3>
  <p>We love sharing our knowledge on Cayman's history and the island's extraordinary marine life.</p>
</article>

<h2 class="about-title abs">About <span>ZOLVATREK</span></h2>
<p class="about-text abs">Lorem ipsum dolor sit amet, consectetur adipiscing elit. Fusce semper vitae leo sit amet vehicula. Sed viverra, justo ac consectetur hendrerit, lacus elit tempor urna, gravida mattis lacus ex sed sem. Nam consectetur, arcu in iaculis dapibus, urna felis congue elit, in consectetur nisi massa sed metus. Lorem ipsum dolor sit amet, consectetur adipiscing elit. Fusce semper vitae leo sit amet vehicula. Sed viverra, justo ac consectetur hendrerit, lacus elit tempor urna, gravida mattis lacus ex sed sem. Nam consectetur.</p>
<div class="btn-outline abs">Read More</div>

<svg class="video-band abs" width="1200" height="680" viewBox="0 0 1200 680" role="img" aria-label="Underwater reef scene behind the video">
  <defs>
    <linearGradient id="reef" x1="0" y1="0" x2="0" y2="1"><stop offset="0" stop-color="#3aa7a3"/><stop offset="1" stop-color="#0f6b68"/></linearGradient>
  </defs>
  <path d="M0 70 C200 20 400 110 600 60 C800 10 1000 100 1200 40 L1200 640 C1000 690 800 600 600 650 C400 700 200 610 0 660 Z" fill="url(#reef)"/>
  <path d="M0 110 C220 60 420 150 620 100 C820 50 1000 140 1200 90 L1200 40 C1000 100 800 10 600 60 C400 110 200 20 0 70 Z" fill="var(--teal)"/>
  <path d="M0 620 C200 570 400 660 600 610 C800 560 1000 650 1200 600 L1200 640 C1000 690 800 600 600 650 C400 700 200 610 0 660 Z" fill="var(--teal)"/>
</svg>
<div class="video-frame abs" role="img" aria-label="Video still of a snorkeler underwater"></div>
<svg class="play abs" viewBox="0 0 90 90"><circle cx="45" cy="45" r="42" fill="rgba(255,255,255,.25)" stroke="#fff" stroke-width="4"/><path d="M36 28l26 17-26 17z" fill="#fff"/></svg>
<h2 class="video-title abs">Private Boat Charter Adventures in the Cayman Islands</h2>
<p class="video-text abs">Lorem ipsum dolor sit amet, consectetur adipiscing elit. Fusce semper vitae leo sit amet vehicula. Sed viverra, justo ac consectetur hendrerit, lacus elit tempor urna, gravida mattis lacus ex sed sem. Nam consectetur.</p>

<h2 class="section-title abs" style="top:1978px">Our <span>PHOTO GALLERY</span></h2>
<div class="gallery-photo abs" role="img" aria-label="Family on a paddle board" style="left:233px;top:2040px;width:378px;height:145px;background:linear-gradient(180deg,#8fd3e6,#2fa8b7)"></div>
<div class="gallery-photo abs" role="img" aria-label="Snorkeler underwater in pink mask" style="left:620px;top:2040px;width:340px;height:145px;background:linear-gradient(180deg,#57b8c7,#1d6f8a)"></div>
<div class="gallery-photo abs" role="img" aria-label="Swimmers by a floating kayak" style="left:233px;top:2192px;width:235px;height:208px;background:linear-gradient(180deg,#5cc8c8,#1a8b8f)"></div>
<div class="gallery-photo abs" role="img" aria-label="Paddle boards lined up on a beach" style="left:475px;top:2192px;width:245px;height:208px;background:linear-gradient(180deg,#b9e2f0,#3fb2c0)"></div>
<div class="gallery-photo abs" role="img" aria-label="Colourful kayaks on the sand" style="left:727px;top:2192px;width:233px;height:208px;background:linear-gradient(180deg,#a9dcea,#2b9aa8)"></div>

<!-- alternating feature strips -->
<section class="strip left abs" style="top:2455px">
  <svg class="band" width="1200" height="307"><polygon points="0,0 600,0 480,307 0,307" fill="var(--teal)"/></svg>
  <div class="circle" role="img" aria-label="Aerial view of a sandbar and shallow lagoon" style="left:233px;background:linear-gradient(180deg,#9ddbe8,#2fa6b3)"></div>
  <div class="copy" style="left:575px;width:540px;top:50px">
    <h2>Your one stop shop for all the rentals you need here in Cayman</h2>
    <p>We have a huge array of fun toys and equipment for you to enjoy. Whether it's for exploring or relaxing, we have all the equipment you need to make the most of your trip here in Cayman. Need something that we don't stock, just ask and we'll do everything we can to get you the gear you need!</p>
  </div>
</section>

<section class="strip right abs" style="top:2762px">
  <svg class="band" width="1200" height="307"><polygon points="720,0 1200,0 1200,307 600,307" fill="var(--lime)"/></svg>
  <div class="circle" role="img" aria-label="Row of kayaks on a white beach" style="left:680px;background:linear-gradient(180deg,#bfe6f0,#3bb0bf)"></div>
  <div class="copy" style="left:70px;width:560px;text-align:center">
    <h2>Check out our interactive map of Cayman</h2>
    <p>You won't find any tourist traps on our map! We're all about getting off the beaten path and finding those unique spots and natural wonders to explore. Get our expert advice on which adventures are best for you and how to tackle them!</p>
  </div>
</section>

<section class="strip left abs" style="top:3069px">
  <svg class="band" width="1200" height="307"><polygon points="0,0 600,0 480,307 0,307" fill="var(--teal)"/></svg>
  <div class="circle" role="img" aria-label="Friends paddling an inflatable kayak" style="left:233px;background:linear-gradient(180deg,#6fcfd0,#1b8e95)"></div>
  <div class="copy" style="left:575px;width:540px;top:85px">
    <h2>Enjoy Complete freedom to explore</h2>
    <p>Inflatable kayaks have revolutionized the way kayak exploration is done in a way never before. Our kayaks give you the freedom to explore Cayman's most secluded locations and snorkel those hard to reach reefs. Our kayaks are light, comfortable and easy to use.</p>
  </div>
</section>

<section class="strip right abs" style="top:3376px">
  <svg class="band" width="1200" height="307"><polygon points="720,0 1200,0 1200,307 600,307" fill="#c9cecc"/></svg>
  <div class="circle" role="img" aria-label="Aerial view of island coastline" style="left:680px;background:linear-gradient(180deg,#4e9fb8,#1d5f78)"></div>
  <div class="copy" style="left:70px;width:560px;text-align:center;top:62px">
    <h2>There's no easier way to get around the island</h2>
    <p>What better way is there to explore the island other than to rent a bike and go? Our mountain bikes are perfect for those interested in heading out on a full day adventure. If you're looking for something more casual, renting a cruiser is perfect to get around the Seven Mile Beach area. Use our map to help guide you to all our suggested locations to explore.</p>
  </div>
</section>

<section class="strip left abs" style="top:3683px">
  <svg class="band" width="1200" height="307"><polygon points="0,0 600,0 480,307 0,307" fill="var(--teal)"/></svg>
  <div class="circle" role="img" aria-label="Family laughing on a kayak" style="left:233px;background:linear-gradient(180deg,#8ad0e4,#2a93a9)"></div>
  <div class="copy" style="left:575px;width:540px;top:65px">
    <h2 style="color:var(--ink)">We want to be your personal concierge and help you to plan out your trip</h2>
    <p>When we come to deliver your equipment, we teach you everything you need to know about the island including the best hidden spots, best restaurants & bars to eat & drink and anything else you might be curious about.</p>
  </div>
</section>

<section class="strip right abs" style="top:3990px">
  <svg class="band" width="1200" height="307"><polygon points="720,0 1200,0 1200,307 600,307" fill="var(--lime)"/></svg>
  <div class="circle" role="img" aria-label="Floating hammock boat on clear water" style="left:680px;background:linear-gradient(180deg,#9be0e0,#2aa3a6)"></div>
  <div class="copy" style="left:70px;width:560px;text-align:right;top:55px">
    <h2>Is it a boat? is it a whale?....<br>It's a Floatnest</h2>
    <p>Easily one of the coolest inventions we've ever come across, the Floatnest is a versatile toy the whole family can enjoy together. Spend the day cruising along Seven Mile Beach in style as you bar hop with your clan. Better still, bring a cooler on board and put the kids to work paddling as you relax in your hammock on the crystal clear waters!</p>
  </div>
</section>

<section class="strip left abs" style="top:4297px">
  <svg class="band" width="1200" height="307"><polygon points="0,0 600,0 480,307 0,307" fill="var(--teal)"/></svg>
  <div class="circle" role="img" aria-label="Snorkeler wearing a full face mask" style="left:233px;background:linear-gradient(180deg,#6ab6cf,#23708c)"></div>
  <div class="copy" style="left:575px;width:540px;top:80px">
    <h2 style="color:var(--ink)">A new way to Snorkel</h2>
    <p>Our full face snorkel masks are easy to use, making them perfect for kids and beginners. You simply put the mask on and breath as you usually would. There's no need to get used to breathing from your mouth and you don't experience a sore jaw from having to hold the mouth piece in place. Just ask and we'll bring one along for you to try!</p>
  </div>
</section>

<h2 class="section-title abs" style="top:4668px">Our <span>ADVENTURE</span> TOP PICKS</h2>
<article class="pick abs" style="left:79px">
  <div class="photo" role="img" aria-label="Glowing blue bioluminescent bay at night" style="background:linear-gradient(180deg,#0b1a3a,#1b6fb5)"></div>
  <h4>Bio Bay</h4><p>Rent everything you need to get outside and explore the island.</p>
</article>
<article class="pick abs" style="left:343px">
  <div class="photo" role="img" aria-label="Sunken shipwreck on the sea floor" style="background:linear-gradient(180deg,#3b8fa8,#1b4d5e)"></div>
  <h4>Kittiwake</h4><p>Rent everything you need to get outside and explore the island.</p>
</article>
<article class="pick abs" style="left:607px">
  <div class="photo" role="img" aria-label="Small sandy cay surrounded by turquoise water" style="background:linear-gradient(180deg,#6cc3d6,#1f8fa3)"></div>
  <h4>Sand Cay Island</h4><p>Rent everything you need to get outside and explore the island.</p>
</article>
<article class="pick abs" style="left:871px">
  <div class="photo" role="img" aria-label="Stingrays gliding over a sandy bottom" style="background:linear-gradient(180deg,#8ec3c4,#3f8c8e)"></div>
  <h4>Stingray City</h4><p>Rent everything you need to get outside and explore the island.</p>
</article>

<footer class="site-footer abs"></footer>
<nav class="footer-nav abs"><span>Home</span><span>Adventure Map</span><span>Rental Gear</span><span>Gallery</span><span>Contact Us</span></nav>
<div class="footer-brand abs"></div>
<div class="footer-name abs">ZOLVATREK</div>
<div class="social abs" style="left:985px" aria-label="Social link"></div>
<div class="social abs" style="left:1033px" aria-label="Social link"></div>
<div class="social abs" style="left:1081px;background:#fff;border:2px solid var(--teal)" aria-label="Social link"></div>
<div class="footer-rule abs"></div>
<div class="contact-item abs" style="left:75px">
  <svg width="22" height="22" viewBox="0 0 24 24"><path d="M12 2C8 2 5 5 5 9c0 5 7 13 7 13s7-8 7-13c0-4-3-7-7-7zm0 9.5A2.5 2.5 0 1 1 12 6.5a2.5 2.5 0 0 1 0 5z" fill="var(--teal)"/></svg>
  <div><b>ZOLVATREK</b><br>123 Building Name, City, Country - zipcode</div>
</div>
<div class="contact-item abs" style="left:585px">
  <svg width="22" height="22" viewBox="0 0 24 24"><path d="M6.6 10.8a15 15 0 0 0 6.6 6.6l2.2-2.2c.3-.3.7-.4 1-.2 1.1.4 2.3.6 3.6.6.6 0 1 .4 1 1V20c0 .6-.4 1-1 1A17 17 0 0 1 3 4c0-.6.4-1 1-1h3.5c.6 0 1 .4 1 1 0 1.3.2 2.5.6 3.6.1.3 0 .7-.2 1z" fill="var(--teal)"/></svg>
  <span>+1 (345) 555 0182</span>
</div>
<div class="contact-item abs" style="left:860px">
  <svg width="22" height="22" viewBox="0 0 24 24"><rect x="2" y="5" width="20" height="14" rx="2" fill="none" stroke="var(--teal)" stroke-width="2"/><path d="M3 6l9 7 9-7" fill="none" stroke="var(--teal)" stroke-width="2"/></svg>
  <span>fun@zolvatrek.com</span>
</div>
<p class="copyright abs">© <b>ZOLVATREK</b> - 2017. All Rights Reserved.</p>

</body>
</html>
```